Gestaltung von Honigetiketten
Zielgruppe
Ich bin ein Imker, der im eigenen Restaurant seinen Honig ausstellen und verkaufen möchte.
Aufgabenstellung
Ich möchte exklusive und edle Honigetiketten die auffallen. Bevorzugt mit den Farben Gold und Schwarz, siehe meinem bisher gesehenen Favoriten im Anhang.
Nur das Logo selbst (Baum) soll übernommen werden Farbe kann variieren, ebenso die Schrift ist variabel.
Auf die Vorderseite des Honigetiketts soll zu lesen sein:
- Deutscher Honig
- Sommertracht
- 500g
- Logo und Name
Auf der Rückseite des Honigetiketts soll zu finden sein:
- freies Feld für Stempel für Namen und Adresse des Abfüllers
- freies Feld für das Mindesthaltbarkeitsdatum

```html
<!DOCTYPE html>
<html lang="de">
<head>
<meta charset="utf-8">
<title>Honigetikett Sommertracht</title>
<link href="https://fonts.googleapis.com/css2?family=Arimo:wght@400;700&family=Great+Vibes&display=swap" rel="stylesheet">
<style>
  :root {
    --page: #f2f2f0;
    --label-black: #050505;
    --gold: #d8b03c;
    --gold-light: #f3d77a;
    --gold-dark: #9c7a1c;
    --honey: #f0a512;
    --white: #ffffff;
    --text-light: #f4f4f4;
  }
  * { box-sizing: border-box; margin: 0; padding: 0; }
  html, body { width: 1200px; height: 1200px; overflow: hidden; }
  body {
    background: var(--page);
    position: relative;
    font-family: "Arimo", Arial, sans-serif;
  }
  .brand-tab {
    position: absolute; left: 488px; top: 132px; width: 244px; height: 182px;
    background: var(--label-black);
    display: flex; flex-direction: column; align-items: center; justify-content: center; gap: 10px;
  }
  .brand-dot {
    width: 26px; height: 26px; border-radius: 50%;
    background: var(--gold);
  }
  .brand-name {
    color: var(--gold); font-weight: 700; font-size: 22px; letter-spacing: 2px;
  }
  .label {
    position: absolute; left: 0; top: 308px; width: 1200px; height: 686px;
    background: var(--label-black);
  }
  .gold-band {
    position: absolute; left: 0; width: 1200px; height: 26px;
    background: linear-gradient(90deg, var(--gold-dark), var(--gold-light) 30%, var(--gold) 55%, var(--gold-light) 80%, var(--gold-dark));
  }
  .gold-band.top { top: 6px; }
  .gold-band.bottom { top: 636px; }
  .honey-drip {
    position: absolute; left: 498px; top: 32px; width: 222px; height: 104px;
    background: linear-gradient(180deg, var(--honey), #c97a06);
    border-radius: 0 0 40px 40px;
    opacity: 0.9;
  }
  .title {
    position: absolute; left: 0; width: 1200px; text-align: center;
  }
  .title.main {
    top: 172px; color: var(--gold); font-weight: 700; font-size: 26px; letter-spacing: 0.5px;
  }
  .title.variety {
    top: 206px; font-family: "Great Vibes", cursive; font-size: 62px; color: var(--gold);
  }
  .blossoms {
    position: absolute; left: 435px; top: 272px;
  }
  .weight {
    position: absolute; left: 0; top: 592px; width: 1216px; text-align: center;
    color: var(--white); font-weight: 700; font-size: 31px; line-height: 36px;
  }
  .producer {
    position: absolute; left: 34px; top: 442px; width: 240px; text-align: center;
    color: var(--text-light); font-size: 20px; line-height: 25px;
  }
  .storage {
    position: absolute; left: 874px; top: 398px; width: 300px; text-align: center;
    color: var(--text-light); font-size: 15px; line-height: 23px;
  }
  .best-before {
    position: absolute; left: 870px; top: 550px; width: 314px; text-align: center;
    color: var(--text-light); font-size: 15px;
  }
  .date-field {
    position: absolute; left: 870px; top: 578px; width: 314px; height: 56px;
    background: var(--white);
  }
</style>
</head>
<body>
  <div class="brand-tab">
    <span class="brand-dot"></span>
    <span class="brand-name">LINDGART</span>
  </div>

  <section class="label">
    <div class="gold-band top"></div>
    <div class="honey-drip" role="img" aria-label="Herabtropfender goldener Honig"></div>

    <p class="title main">DEUTSCHER HONIG</p>
    <p class="title variety">Sommertracht</p>

    <svg class="blossoms" width="330" height="302" viewBox="0 0 360 330" role="img" aria-label="Drei goldene Waben mit gemalten Blättern und einer blauen Blüte">
      <g fill="none" stroke="#d8b03c" stroke-width="2">
        <polygon points="103,19 180,63 180,152 103,196 26,152 26,63" fill="#2a1a12"/>
        <polygon points="256,11 333,55 333,144 256,188 179,144 179,55" fill="#1b3a6a"/>
        <polygon points="176,151 253,195 253,284 176,328 99,284 99,195" fill="#24160f"/>
      </g>
    </svg>

    <p class="weight">500 g</p>

    <p class="producer">Herstellung:<br>Lindauer Weg 14<br>91286 Talbrunn<br>an der Wiesent<br>Telefon: 09187 4410</p>

    <p class="storage">DEUTSCHER BIENENHONIG<br>TROCKEN, KÜHL<br>und DUNKEL LAGERN!</p>
    <p class="best-before">MINDESTENS HALTBAR BIS:</p>
    <div class="date-field"></div>

    <div class="gold-band bottom"></div>
  </section>
</body>
</html>
```